social interest sharing site needs a web site design

we need a web site design for a social web platform.
the site is one page(main page), that is split into 3 sections
each section is a different color(red,green and blue)
and a user can choose to share each of the sections.
any section/color will contain boxes , each box can contain different media types.

the media types:
* list of URLS
* list of articles including title + image + description
* list of videos
* thumbnails of images
* calender
* list of emails

the main content will look like corkboardly layout
multiple boxes each box can contain different type of content as described above

each color is a different tab
each tab will have layout like corkboardly
Updates

please read the last description update.
and i uploaded an image that can explain the requirements better

thanks
Oren
 

Industry/Entity Type

Media

```html
<!DOCTYPE html>
<html lang="en">
<head>
<meta charset="utf-8">
<title>hueboard — share the creativity</title>
<link href="https://fonts.googleapis.com/css2?family=Raleway:wght@300;400;600;700&family=Roboto+Condensed:wght@400;700&family=Roboto:wght@400;700&display=swap" rel="stylesheet">
<style>
:root{
  --page:#f1f1f1;
  --white:#ffffff;
  --ink:#3a3a3a;
  --grey:#8b8b8b;
  --blue:#00a7e6;
  --blue-dark:#0090c8;
  --purple:#9530ee;
  --purple-row:#a26bd4;
  --orange:#f7882e;
  --green:#27ae5f;
  --red-title:#c4151c;
  --nav-blue:#1c5d8a;
  --share-a:#3b5a98;
  --share-b:#27a9e1;
  --share-c:#f26d4b;
}
*{box-sizing:border-box;margin:0;padding:0}
html,body{width:1200px;height:2240px;overflow:hidden;background:var(--page)}
body{position:relative;font-family:"Roboto",Arial,sans-serif;color:var(--ink)}

/* header */
.top-social{position:absolute;top:28px;left:940px;display:flex;gap:8px}
.top-social span{width:22px;height:22px;border-radius:50%;background:#1d1d1d}
.nav-bar{position:absolute;top:67px;left:0;width:1200px;height:67px;background:var(--white)}
.nav-link{position:absolute;top:95px;font-family:"Raleway",sans-serif;font-size:13px;font-weight:600;letter-spacing:.5px;color:var(--grey)}
.nav-link.active{color:var(--nav-blue)}
.search-btn{position:absolute;top:84px;left:985px;width:36px;height:34px;background:var(--blue)}
.brand-plaque{position:absolute;top:20px;left:400px;width:400px;height:148px;background:linear-gradient(180deg,#f6f6f6,#ececec);border-radius:22px}
.brand{position:absolute;top:66px;left:400px;width:400px;display:flex;align-items:center;justify-content:center;gap:14px}
.brand-dot{width:44px;height:44px;border-radius:50%;background:var(--blue)}
.brand-name{font-family:"Raleway",sans-serif;font-weight:600;font-size:44px;color:#4a4a4a;letter-spacing:-.5px}

/* hero */
.hero-kicker{position:absolute;top:222px;left:0;width:1200px;text-align:center;font-family:"Raleway",sans-serif;font-weight:300;font-size:33px;color:#7a7a7a;letter-spacing:1px}
.hero-title{position:absolute;top:264px;left:0;width:1200px;text-align:center;font-family:"Raleway",sans-serif;font-weight:400;font-size:44px;color:var(--blue);letter-spacing:.5px}
.hero-art{position:absolute;top:352px;left:112px;width:976px;height:299px;border-radius:6px 6px 0 0;
  background:linear-gradient(90deg,#f6e2d2 0%,#e3dcf2 28%,#d9e9f3 50%,#dcecf3 72%,#f5e4d6 100%)}

/* sections */
.band{position:absolute;left:0;width:1200px}
.band.videos{top:651px;height:426px;background:var(--blue)}
.band.links{top:1077px;height:313px;background:var(--purple)}
.band.articles{top:1390px;height:426px;background:var(--orange)}
.band.photos{top:1816px;height:312px;background:var(--green)}
.badge{position:absolute;left:464px;width:88px;height:88px;border-radius:50%;background:rgba(255,255,255,.28);display:flex;align-items:center;justify-content:center}
.badge-core{width:66px;height:66px;border-radius:50%;display:flex;align-items:center;justify-content:center}
.section-title{position:absolute;left:554px;font-family:"Raleway",sans-serif;font-weight:300;font-size:37px;color:var(--white);letter-spacing:1px}
.chev{position:absolute}
.dots{position:absolute;left:0;width:1200px;display:flex;justify-content:center;gap:6px}
.dots span{width:7px;height:7px;border-radius:50%;background:var(--white)}
.dots span.on{background:rgba(255,255,255,.45);box-shadow:inset 0 0 0 2px var(--white)}

/* media cards */
.card{position:absolute;background:var(--white);box-shadow:0 2px 6px rgba(0,0,0,.3)}
.card-title{font-family:"Roboto Condensed",sans-serif;font-size:19px;color:var(--red-title);text-transform:uppercase;line-height:1.05}
.card-desc{font-size:9.5px;line-height:1.35;color:#9a9a9a}
.tools{position:absolute;right:0;top:0;width:74px;background:#e5e5e5}
.tools-row{display:flex;height:25px;align-items:center;justify-content:space-around;background:#e9e9e9}
.tools-row.share{background:#dcdcdc;justify-content:flex-start}
.tools-row.share span{width:24px;height:25px;border-right:1px solid #fff}
.s-a{background:var(--share-a)}.s-b{background:var(--share-b)}.s-c{background:var(--share-c)}
.media{position:absolute;left:0;right:0;bottom:0}
.play{position:absolute;left:50%;top:50%;width:60px;height:60px;margin:-30px 0 0 -30px;border-radius:50%;background:rgba(120,120,120,.6)}

/* links */
.link-col{position:absolute;top:1180px;width:403px}
.link-row{height:21px;margin-bottom:4.5px;background:var(--purple-row);display:flex;align-items:center;font-size:10.5px;color:var(--white);padding:0 8px}
.link-row b{margin:0 6px 0 8px}
.link-row .txt{flex:1;white-space:nowrap;overflow:hidden}
.link-row .plus{font-size:16px;font-weight:700}
.chain{width:10px;height:6px;border:1.5px solid #e8dcf8;border-radius:3px;transform:rotate(-40deg)}

/* articles */
.art-card .photo{position:absolute;left:0;top:0;width:207px;height:151px}
.art-card .corner{position:absolute;right:0;top:0;width:0;height:0;border-top:22px solid #111;border-left:22px solid transparent}
.art-card .date{font-size:10px;color:#777}
.art-card .date em{font-style:normal;color:var(--red-title)}

/* photos */
.photo-strip{position:absolute;top:1920px;left:168px;display:flex;gap:2px}
.photo-strip div{width:170px;height:168px}

.footer{position:absolute;top:2153px;left:0;width:1200px;text-align:center;font-size:10px;letter-spacing:.4px;color:#777}
</style>
</head>
<body>

<!-- header -->
<div class="top-social"><span></span><span></span><span></span></div>
<div class="nav-bar"></div>
<div class="brand-plaque" role="img" aria-label="Decorative framed plaque behind the site name"></div>
<div class="brand"><span class="brand-dot"></span><span class="brand-name">hueboard</span></div>
<a class="nav-link active" style="left:168px">ABOUT HUEBOARD</a>
<a class="nav-link" style="left:332px">BLOG</a>
<a class="nav-link" style="left:815px">FEATURES</a>
<a class="nav-link" style="left:911px">PRESS</a>
<div class="search-btn">
  <svg width="36" height="34" viewBox="0 0 36 34"><circle cx="17" cy="15" r="5" fill="none" stroke="#fff" stroke-width="2"/><line x1="21" y1="19" x2="24" y2="22" stroke="#fff" stroke-width="2.4"/></svg>
</div>

<!-- hero -->
<div class="hero-kicker">SHARE THE CREATIVITY</div>
<div class="hero-title">YOU’VE ALWAYS WANTED TO FINISH</div>
<div class="hero-art" role="img" aria-label="Illustration of a smartphone showing the app surrounded by a network of connected coloured media icons"></div>

<!-- VIDEOS -->
<section class="band videos">
  <div class="badge" style="top:6px"><div class="badge-core" style="background:var(--blue-dark)">
    <svg width="34" height="28" viewBox="0 0 34 28"><rect x="2" y="10" width="30" height="16" fill="#fff"/><path d="M2 3 L30 3 L30 9 L2 9z" fill="#fff"/><path d="M8 3 L12 9 M16 3 L20 9 M24 3 L28 9" stroke="var(--blue-dark)" stroke-width="2"/></svg>
  </div></div>
  <div class="section-title" style="top:26px">VIDEOS</div>
  <svg class="chev" style="left:56px;top:210px" width="34" height="76"><path d="M32 2 L3 38 L32 74" fill="none" stroke="#fff" stroke-width="1.5"/></svg>
  <svg class="chev" style="left:1108px;top:210px" width="34" height="76"><path d="M2 2 L31 38 L2 74" fill="none" stroke="#fff" stroke-width="1.5"/></svg>
  <div class="dots" style="top:402px"><span></span><span class="on"></span><span></span><span></span></div>
</section>

<article class="card" style="left:159px;top:754px;width:272px;height:278px">
  <div style="padding:10px 14px"><div class="card-title">Cyber Monday</div><p class="card-desc" style="width:170px;margin-top:5px">Comparing this year's Cyber Monday with the same day last...</p></div>
  <div class="tools"><div class="tools-row">▣ ♥ ☁</div><div class="tools-row share"><span class="s-a"></span><span class="s-b"></span><span class="s-c"></span></div></div>
  <div class="media" role="img" aria-label="Video still of a latte with foam art on a wooden table" style="top:78px;background:linear-gradient(135deg,#8a5a3a,#5e3a22 60%,#3b2414)"><span class="play"></span></div>
</article>
<article class="card" style="left:461px;top:754px;width:272px;height:278px">
  <div style="padding:10px 14px"><div class="card-title">Cyber Monday</div><p class="card-desc" style="width:170px;margin-top:5px">Comparing this year's Cyber Monday with the same day last...</p></div>
  <div class="tools"><div class="tools-row">▣ ♥ ☁</div><div class="tools-row share"><span class="s-a"></span><span class="s-b"></span><span class="s-c"></span></div></div>
  <div class="media" role="img" aria-label="Video still of a coffee shop counter with a chalkboard menu" style="top:78px;background:linear-gradient(180deg,#3a4447,#6f7a78 55%,#cfd2cc)"><span class="play"></span></div>
</article>
<article class="card" style="left:765px;top:754px;width:274px;height:278px">
  <div style="padding:10px 14px"><div class="card-title">Cyber Monday</div><p class="card-desc" style="width:170px;margin-top:5px">Comparing this year's Cyber Monday with the same day last...</p></div>
  <div class="tools"><div class="tools-row">▣ ♥ ☁</div><div class="tools-row share"><span class="s-a"></span><span class="s-b"></span><span class="s-c"></span></div></div>
  <div class="media" role="img" aria-label="Video still looking down from a rooftop onto a city at dusk" style="top:78px;background:linear-gradient(160deg,#556b8a,#3d4a5c 50%,#8a6a4a)"></div>
</article>

<!-- LINKS -->
<section class="band links">
  <div class="badge" style="top:6px"><div class="badge-core" style="background:#7d1fd0">
    <svg width="30" height="30" viewBox="0 0 30 30"><circle cx="15" cy="15" r="12" fill="none" stroke="#fff" stroke-width="2.5"/><ellipse cx="15" cy="15" rx="5" ry="12" fill="none" stroke="#fff" stroke-width="2"/><line x1="3" y1="15" x2="27" y2="15" stroke="#fff" stroke-width="2"/></svg>
  </div></div>
  <div class="section-title" style="top:26px">LINKS</div>
  <svg class="chev" style="left:56px;top:170px" width="34" height="76"><path d="M32 2 L3 38 L32 74" fill="none" stroke="#fff" stroke-width="1.5"/></svg>
  <svg class="chev" style="left:1108px;top:170px" width="34" height="76"><path d="M2 2 L31 38 L2 74" fill="none" stroke="#fff" stroke-width="1.5"/></svg>
  <div class="dots" style="top:289px"><span class="on"></span><span></span><span></span></div>
</section>

<div class="link-col" style="left:168px">
  <div class="link-row"><i class="chain"></i><b>10.13</b><span class="txt">Handheld Design Sourcebook features Plumleaf.com site</span><span class="plus">+</span></div>
  <div class="link-row"><i class="chain"></i><b>01.13</b><span class="txt">Finalist in the 2012 Bitmark Awards – Plumleaf Design website</span><span class="plus">+</span></div>
  <div class="link-row"><i class="chain"></i><b>03.12</b><span class="txt">Forge Magazine includes Plumleaf.com in portfolios article</span><span class="plus">+</span></div>
  <div class="link-row"><i class="chain"></i><b>02.12</b><span class="txt">23 Amazing Single Page Websites includes Plumleaf.com</span><span class="plus">+</span></div>
  <div class="link-row"><i class="chain"></i><b>01.12</b><span class="txt">Peerless Style features Plumleaf.com in gallery</span><span class="plus">+</span></div>
  <div class="link-row"><i class="chain"></i><b>12.11</b><span class="txt">Scoutline features Plumleaf.com in web design showcase</span><span class="plus">+</span></div>
</div>
<div class="link-col" style="left:612px">
  <div class="link-row"><i class="chain"></i><b>10.13</b><span class="txt">Handheld Design Sourcebook features Plumleaf.com site</span><span class="plus">+</span></div>
  <div class="link-row"><i class="chain"></i><b>01.13</b><span class="txt">Finalist in the 2012 Bitmark Awards – Plumleaf Design website</span><span class="plus">+</span></div>
  <div class="link-row"><i class="chain"></i><b>03.12</b><span class="txt">Forge Magazine includes Plumleaf.com in portfolios article</span><span class="plus">+</span></div>
  <div class="link-row"><i class="chain"></i><b>02.12</b><span class="txt">23 Amazing Single Page Websites includes Plumleaf.com</span><span class="plus">+</span></div>
  <div class="link-row"><i class="chain"></i><b>01.12</b><span class="txt">Peerless Style features Plumleaf.com in gallery</span><span class="plus">+</span></div>
  <div class="link-row"><i class="chain"></i><b>12.11</b><span class="txt">Scoutline features Plumleaf.com in web design showcase</span><span class="plus">+</span></div>
</div>

<!-- ARTICLES -->
<section class="band articles">
  <div class="badge" style="top:0"><div class="badge-core" style="background:#f2a531">
    <svg width="30" height="30" viewBox="0 0 30 30"><rect x="3" y="6" width="21" height="21" rx="2" fill="none" stroke="#fff" stroke-width="2.5"/><path d="M12 19 L13 14 L25 2 L29 6 L17 18z" fill="#fff"/></svg>
  </div></div>
  <div class="section-title" style="top:22px">ARTICLES</div>
  <svg class="chev" style="left:56px;top:200px" width="34" height="76"><path d="M32 2 L3 38 L32 74" fill="none" stroke="#fff" stroke-width="1.5"/></svg>
  <svg class="chev" style="left:1108px;top:200px" width="34" height="76"><path d="M2 2 L31 38 L2 74" fill="none" stroke="#fff" stroke-width="1.5"/></svg>
  <div class="dots" style="top:400px"><span></span><span class="on"></span><span></span><span></span></div>
</section>

<article class="card art-card" style="left:166px;top:1486px;width:207px;height:287px">
  <div class="photo" role="img" aria-label="Portrait photo of a smiling woman against a red patterned wall" style="background:linear-gradient(135deg,#ff5a1a,#e8380f)"></div><span class="corner"></span>
  <div style="position:absolute;top:165px;left:16px"><div class="card-title">Cyber<br>Monday</div></div>
  <div class="tools" style="top:151px"><div class="tools-row">▣ ♥ ☁</div><div class="tools-row share"><span class="s-a"></span><span class="s-b"></span><span class="s-c"></span></div></div>
  <p class="card-desc" style="position:absolute;top:220px;left:16px;width:180px">Comparing this year's Cyber Monday with the same day last...</p>
  <p class="date" style="position:absolute;top:256px;left:16px">17/12/2013 in: <em>News</em></p>
</article>
<article class="card art-card" style="left:383px;top:1486px;width:207px;height:287px">
  <div class="photo" role="img" aria-label="Photo of a bowl of creamy soup with a herb garnish" style="background:linear-gradient(180deg,#b5722f,#e9dcc2 55%,#f6f1e7)"></div><span class="corner"></span>
  <div style="position:absolute;top:165px;left:16px"><div class="card-title">Cyber<br>Monday</div></div>
  <div class="tools" style="top:151px"><div class="tools-row">▣ ♥ ☁</div><div class="tools-row share"><span class="s-a"></span><span class="s-b"></span><span class="s-c"></span></div></div>
  <p class="card-desc" style="position:absolute;top:220px;left:16px;width:180px">Comparing this year's Cyber Monday with the same day last...</p>
  <p class="date" style="position:absolute;top:256px;left:16px">17/12/2013 in: <em>News</em></p>
</article>
<article class="card art-card" style="left:597px;top:1486px;width:207px;height:287px">
  <div class="photo" role="img" aria-label="Photo of a row of brick townhouses under a pale sky" style="background:linear-gradient(180deg,#c9d3df,#7a6a5e 60%,#4a3d36)"></div><span class="corner"></span>
  <div style="position:absolute;top:165px;left:16px"><div class="card-title">Cyber<br>Monday</div></div>
  <div class="tools" style="top:151px"><div class="tools-row">▣ ♥ ☁</div><div class="tools-row share"><span class="s-a"></span><span class="s-b"></span><span class="s-c"></span></div></div>
  <p class="card-desc" style="position:absolute;top:220px;left:16px;width:180px">Comparing this year's Cyber Monday with the same day last...</p>
  <p class="date" style="position:absolute;top:256px;left:16px">17/12/2013 in: <em>News</em></p>
</article>
<article class="card art-card" style="left:814px;top:1486px;width:207px;height:287px">
  <div class="photo" role="img" aria-label="Photo of a bright living room with people relaxing on a sofa" style="background:linear-gradient(160deg,#efe6d8,#d8c8b0 60%,#a89378)"></div><span class="corner"></span>
  <div style="position:absolute;top:165px;left:16px"><div class="card-title">Cyber<br>Monday</div></div>
  <div class="tools" style="top:151px"><div class="tools-row">▣ ♥ ☁</div><div class="tools-row share"><span class="s-a"></span><span class="s-b"></span><span class="s-c"></span></div></div>
  <p class="card-desc" style="position:absolute;top:220px;left:16px;width:180px">Comparing this year's Cyber Monday with the same day last...</p>
  <p class="date" style="position:absolute;top:256px;left:16px">17/12/2013 in: <em>News</em></p>
</article>

<!-- PHOTOS -->
<section class="band photos">
  <div class="badge" style="top:2px"><div class="badge-core" style="background:#58c477">
    <svg width="32" height="32" viewBox="0 0 32 32"><rect x="5" y="4" width="18" height="23" rx="2" fill="none" stroke="#fff" stroke-width="2.5" transform="rotate(-10 14 16)"/><rect x="10" y="6" width="18" height="23" rx="2" fill="#58c477" stroke="#fff" stroke-width="2.5" transform="rotate(8 19 17)"/></svg>
  </div></div>
  <div class="section-title" style="top:24px">PHOTOS</div>
  <svg class="chev" style="left:56px;top:156px" width="34" height="76"><path d="M32 2 L3 38 L32 74" fill="none" stroke="#fff" stroke-width="1.5"/></svg>
  <svg class="chev" style="left:1108px;top:156px" width="34" height="76"><path d="M2 2 L31 38 L2 74" fill="none" stroke="#fff" stroke-width="1.5"/></svg>
  <div class="dots" style="top:290px"><span></span><span class="on"></span><span></span><span></span></div>
</section>

<div class="photo-strip">
  <div role="img" aria-label="Photo of a bright room with window shutters and a plant" style="background:linear-gradient(135deg,#e9e9e6,#9d9f99)"></div>
  <div role="img" aria-label="Photo of two people sharing a drink at a party" style="background:linear-gradient(135deg,#3a2a1c,#b27a3a 60%,#e0b070)"></div>
  <div role="img" aria-label="Photo of a snowy winter scene with a small snowman" style="background:linear-gradient(180deg,#f4f6f7,#d6dcdf)"></div>
  <div role="img" aria-label="Photo of a jockey racing a horse" style="background:linear-gradient(160deg,#5c7a9a,#2d3a2f 55%,#d46a22)"></div>
  <div role="img" aria-label="Photo of a group in bright colourful hoods" style="background:linear-gradient(135deg,#8a2a6a,#d6c92c 45%,#2c8a4a)"></div>
</div>

<footer class="footer">©2013 hueboard. ALL RIGHTS RESERVED.</footer>

</body>
</html>
```